Web-page design

We need a initial web design for our page kelbrook.com.au (which is not yet set up).
We provide consulting services for all kinds of problems in and between organisations.
Main focus is on conflict resolution but we also support companies on improving their operational performance.
We want to have the following page structure (and part of the project is to design the 8 pages):
- Home
- Services (we offer 3 main service areas - one per page)
- Case studies (one per page)
- Engaging us (our process)
- About Conflict & low performance
- Conflict resolution App
- About
- Contact (Email form)
- Our logo should be on each page.
The start page should include the following information:
- Twitter / Linkedin / facebook/ google + Links
- Telephone / Email or in general contact details
- News
- A quite prominent picture box with 3 alternating pics - each representing one of our service areas
- Link to our App
- Testimonials
It would be nice if the service pages would have an image header. Links to the information section (about conflict & low performance; and the app page) would be nice as well.
We like the following joomla designs: www.frandelthemes.com/itempreview/153
No need to copy it, it should just give you an idea.
We like the layout here with the picture and space for the case studies on the left. Somewhere beneath should be the 3 service areas with a picture each.
In terms of colors: our logo colours are Blue (RBG 8;44;80) and Orange (RGB 231;120;23). The orange could be used to emphasise certain things, however there should not be too much color.
Budget for images available, so please use placeholders or ask us for specific photos/images, if you need them for your design.
Updates
Hi, one more thing that we would like to have is the case studies not hidden behind a link "case studies" - we would like to have them individually linked prominent on the first page. There will be about 6-8 of them. Thats what we liked on the joomla template (the links left from the picture).
Hi, thanks very much for all the great proposals.
We are currently going through the selection process and will post our decision early next week.
Thanks again!
Wilma
Target Market(s)
- target customers are all different kinds of businesses and organisations (all industries, government, non-for-profit, ...) experiencing conflict and tension - be it with internal staff, amongst managers or board members, dysfunctional teams, between organizations or customers and organizations... examples could be bullying allegations, governmental negotiations with unions, disputes within organizations etc.
- also we will offer performance improvement services for organizations
- we will offer mediation, facilitation, negotiation, performance improvement services, conflict coaching, conflict management, change management services
- if comparable to anything - then to a law firm in terms of dealing with conflicts but its much less adversarial and much more about the people and their interests rather than about laws
- basically it's all kind of things you can do in order to solve disputes without involving lawyers and a court - so it's much cheaper and target is to find a solution all parties can live with rather than having a judge deciding about who wins and who looses
- performance management is more about analysing reasons for a lack of performance and setting up continous improvement systems, supporting change management, facilitating improvement workshops or strategic meetings, ...
Industry/Entity Type
Consulting
Look and feel

```html
<!DOCTYPE html>
<html lang="en">
<head>
<meta charset="utf-8">
<title>Harlow Brennan – Conflict Resolution &amp; Performance Consulting</title>
<link href="https://fonts.googleapis.com/css2?family=Ubuntu:ital,wght@0,300;0,400;0,500;1,400&family=Ubuntu+Condensed&family=Open+Sans:wght@400;600&display=swap" rel="stylesheet">
<style>
  :root {
    --navy: #082c50;
    --orange: #e77817;
    --ink: #333333;
    --muted: #666666;
    --soft: #999999;
    --rule: #d9d9d9;
    --band: #f1f1f1;
    --footer: #4a4a4a;
    --footer-deep: #3e3e3e;
    --footer-text: #e6e6e6;
    --white: #ffffff;
  }
  * { box-sizing: border-box; margin: 0; padding: 0; }
  html, body { width: 928px; height: 1200px; overflow: hidden; }
  body {
    position: relative;
    background: var(--white);
    font-family: "Ubuntu", "Open Sans", sans-serif;
    color: var(--ink);
  }
  a { color: inherit; text-decoration: none; }
  .abs { position: absolute; }

  /* Header */
  .top-bar { position: absolute; left: 0; top: 0; width: 928px; height: 3px; background: var(--orange); }
  .site-header {
    position: absolute; left: 0; top: 3px; width: 928px; height: 87px;
    background: linear-gradient(180deg, #f6f6f6 0%, #ffffff 100%);
  }
  .brand { position: absolute; left: 78px; top: 28px; display: flex; align-items: center; gap: 8px; }
  .brand-mark { width: 14px; height: 14px; background: var(--orange); }
  .brand-name { font-size: 24px; font-weight: 400; color: var(--navy); letter-spacing: 0.5px; }
  .brand-url { position: absolute; left: 96px; top: 63px; font-size: 10px; color: var(--navy); letter-spacing: 6.4px; }
  .header-contact { position: absolute; right: 78px; top: 19px; display: flex; gap: 14px; font-size: 9px; color: var(--soft); }
  .header-contact span { display: flex; align-items: center; gap: 5px; }
  .social-circles { position: absolute; right: 78px; top: 50px; display: flex; gap: 7px; }
  .social-circles span { width: 24px; height: 24px; border-radius: 50%; background: var(--navy); }
  .social-circles span:nth-child(2) { background: #2a9ad6; }
  .social-circles span:nth-child(3) { background: #1c6ca8; }
  .social-circles span:nth-child(4) { background: #c2362a; }

  /* Navigation */
  .main-nav {
    position: absolute; left: 0; top: 90px; width: 928px; height: 38px;
    background: var(--navy); display: flex; padding-left: 78px;
  }
  .main-nav a { color: var(--white); font-size: 11.5px; line-height: 38px; padding: 0 14px; }
  .main-nav a.is-active { background: var(--orange); }

  /* Slider */
  .hero-frame {
    position: absolute; left: 78px; top: 137px; width: 772px; height: 259px;
    background: var(--white); border: 1px solid #e2e2e2; box-shadow: 0 1px 3px rgba(0,0,0,.12);
  }
  .hero-photo {
    position: absolute; left: 7px; top: 7px; width: 757px; height: 243px;
    background: linear-gradient(100deg, #3a3a2a 0%, #8c8a55 35%, #c3c06c 60%, #2e2a24 100%);
  }
  .hero-caption {
    position: absolute; left: 23px; top: 24px; width: 232px; height: 115px;
    background: rgba(60,60,45,.72); padding: 16px 18px; color: var(--white);
  }
  .hero-caption h2 { font-size: 15px; font-weight: 400; margin-bottom: 6px; }
  .hero-caption p { font-size: 9.5px; line-height: 15.5px; }
  .hero-dots { position: absolute; left: 15px; top: 215px; display: flex; gap: 5px; }
  .hero-dots span { width: 11px; height: 11px; border-radius: 50%; background: var(--white); }
  .hero-dots span.is-current { background: var(--orange); }

  /* Services */
  .section-title {
    position: absolute; left: 78px; top: 405px; width: 772px; height: 30px;
    border-bottom: 1px solid var(--rule);
    font-family: "Ubuntu Condensed", "Ubuntu", sans-serif; font-size: 19px; color: var(--navy);
  }
  .section-title span { display: inline-block; height: 30px; border-bottom: 2px solid var(--orange); padding-right: 2px; }
  .service-card { position: absolute; top: 450px; width: 231px; }
  .service-photo { width: 231px; height: 115px; border: 3px solid var(--white); outline: 1px solid #e0e0e0; }
  .service-card h3 {
    margin-top: 7px; font-size: 13.5px; font-weight: 400; color: var(--navy);
    border-bottom: 1px solid var(--rule); padding-bottom: 4px; position: relative;
  }
  .service-card h3::after { content: ""; position: absolute; left: 0; bottom: -1px; width: 110px; height: 2px; background: var(--orange); }
  .service-card p { margin-top: 10px; font-size: 9.8px; line-height: 15.5px; color: var(--muted); }
  .read-more { display: flex; justify-content: flex-end; align-items: center; gap: 5px; margin-top: 6px; font-size: 10px; color: var(--navy); }
  .col-divider { position: absolute; top: 450px; width: 0; height: 220px; border-left: 1px dashed #dddddd; }

  /* News & testimonials band */
  .info-band { position: absolute; left: 0; top: 690px; width: 928px; height: 248px; background: var(--band); }
  .band-title { position: absolute; top: 708px; font-size: 16px; color: var(--ink); }
  .news-item { position: absolute; left: 108px; width: 345px; height: 80px; }
  .news-thumb { position: absolute; left: 0; top: 0; width: 108px; height: 80px; border: 3px solid #dddddd; }
  .news-body { position: absolute; left: 124px; top: -2px; width: 225px; }
  .news-body h4 { font-family: "Open Sans", sans-serif; font-size: 9.5px; font-weight: 600; color: #333; }
  .news-meta { display: flex; gap: 14px; margin-top: 7px; font-family: "Open Sans", sans-serif; font-size: 7.5px; color: var(--soft); }
  .news-meta span { display: flex; align-items: center; gap: 4px; }
  .news-body p { margin-top: 9px; font-family: "Open Sans", sans-serif; font-size: 8px; line-height: 14px; color: var(--soft); }
  .news-link { display: block; margin-top: 6px; font-family: "Open Sans", sans-serif; font-size: 8.5px; color: var(--orange); }

  .testimonial-box {
    position: absolute; left: 474px; top: 742px; width: 345px; height: 174px;
    background: var(--white); border-radius: 3px;
  }
  .testimonial-tail { position: absolute; left: 580px; top: 722px; }
  .testimonial-arrow { position: absolute; top: 25px; width: 22px; height: 22px; background: #f3f3f3; display: flex; align-items: center; justify-content: center; }
  .testimonial-line { position: absolute; top: 36px; width: 232px; left: 57px; border-top: 3px double #e8e8e8; }
  .avatar {
    position: absolute; left: 134px; top: 8px; width: 78px; height: 78px; border-radius: 50%;
    border: 3px solid #d9a520; background: radial-gradient(circle, #e9e3dc 0%, #b9b0a6 100%);
  }
  .testimonial-box blockquote {
    position: absolute; left: 20px; top: 100px; width: 305px; text-align: center;
    font-family: "Open Sans", sans-serif; font-size: 8.6px; line-height: 15.5px; color: #444;
  }
  .testimonial-author { position: absolute; left: 0; top: 153px; width: 345px; text-align: center; font-size: 9.5px; color: #222; }
  .testimonial-author em { font-style: italic; }

  /* Footer */
  .footer-rule { position: absolute; left: 0; top: 964px; width: 928px; height: 2px; background: var(--orange); }
  .site-footer { position: absolute; left: 0; top: 966px; width: 928px; height: 174px; background: var(--footer); color: var(--footer-text); }
  .footer-col { position: absolute; top: 20px; font-size: 9.3px; line-height: 18.5px; }
  .footer-col h5 { font-size: 12px; font-weight: 400; color: var(--white); margin-bottom: 8px; line-height: 16px; }
  .footer-col li { list-style: none; }
  .footer-col li::before { content: "» "; }
  .footer-col address { font-style: normal; line-height: 14px; }
  .footer-divider { position: absolute; top: 20px; height: 127px; border-left: 1px solid #5c5c5c; }
  .newsletter-input {
    margin-top: 10px; width: 212px; height: 26px; background: var(--white); border: 1px solid #ccc;
    font-size: 9px; color: #555; padding: 0 7px; line-height: 24px;
  }
  .newsletter-btn {
    margin: 9px 0 0 134px; width: 78px; height: 24px; background: var(--orange); color: var(--white);
    font-size: 10.5px; text-align: center; line-height: 24px;
  }
  .footer-bottom { position: absolute; left: 0; top: 1140px; width: 928px; height: 60px; background: var(--footer-deep); }
  .copyright { position: absolute; left: 78px; top: 24px; font-size: 9.8px; color: var(--footer-text); }
  .footer-social { position: absolute; right: 78px; top: 19px; display: flex; gap: 5px; }
  .footer-social span { width: 20px; height: 20px; border: 1px solid #6a6a6a; background: #555; }
</style>
</head>
<body>
  <div class="top-bar"></div>

  <header class="site-header">
    <a class="brand" href="#"><span class="brand-mark"></span><span class="brand-name">HARLOW BRENNAN</span></a>
    <div class="brand-url">www.kelbrook.com.au</div>
    <div class="header-contact">
      <span>
        <svg width="13" height="9" viewBox="0 0 13 9"><rect x=".5" y=".5" width="12" height="8" fill="none" stroke="#aaa"/><path d="M.5 .5l6 4.5 6-4.5" fill="none" stroke="#aaa"/></svg>
        info@kelbrook.com.au
      </span>
      <span>
        <svg width="12" height="10" viewBox="0 0 12 10"><path d="M1 3c0-2 10-2 10 0v1H8V3H4v1H1z" fill="#aaa"/><rect x="2" y="5" width="8" height="4" rx="1" fill="#aaa"/></svg>
        1200-555-0190
      </span>
    </div>
    <div class="social-circles" aria-label="Social links"><span></span><span></span><span></span><span></span></div>
  </header>

  <nav class="main-nav">
    <a class="is-active" href="#">Home</a>
    <a href="#">About</a>
    <a href="#">Services</a>
    <a href="#">Case studies</a>
    <a href="#">Engaging us</a>
    <a href="#">About Conflict &amp; low performance</a>
    <a href="#">Conflict resolution App</a>
    <a href="#">Contact</a>
  </nav>

  <section class="hero-frame">
    <div class="hero-photo" role="img" aria-label="Photo of a young girl at a table with an adult's hand reaching towards her">
      <div class="hero-caption">
        <h2>Lorem ipsum dolor sit amet</h2>
        <p>Nam sit amet dapibus neque. Integer tristique neque lacus, id egestas odio fermentum non. Curabitur sit amet hendrerit diam. In in laoreet lectus, vel sollicitudin velit.</p>
      </div>
      <div class="hero-dots"><span class="is-current"></span><span></span><span></span><span></span></div>
    </div>
  </section>

  <h2 class="section-title"><span>Our Services</span></h2>

  <article class="service-card" style="left:78px">
    <div class="service-photo" role="img" aria-label="Photo of children handing items into a donations box" style="background:linear-gradient(120deg,#c8748a,#86a858 55%,#c9bca8)"></div>
    <h3>Lorem ipsum dolor</h3>
    <p>Vestibulum fermentum ultrices risus id commodo. Fusce sed ipsum ut est porta faucibus vitae luctus felis. Integer adipiscing imperdiet neque..</p>
    <a class="read-more" href="#"><svg width="11" height="11" viewBox="0 0 11 11"><circle cx="5.5" cy="5.5" r="5.5" fill="#082c50"/><path d="M5.5 3v5M3 5.5h5" stroke="#fff" stroke-width="1.4"/></svg>Read More</a>
  </article>
  <div class="col-divider" style="left:329px"></div>

  <article class="service-card" style="left:348px">
    <div class="service-photo" role="img" aria-label="Photo of volunteers walking and carrying supplies down a street" style="background:linear-gradient(120deg,#6e6e70,#a08070 50%,#d37a40 75%,#5a5a5a)"></div>
    <h3>Lorem ipsum dolor</h3>
    <p>Vestibulum fermentum ultrices risus id commodo. Fusce sed ipsum ut est porta faucibus vitae luctus felis. Integer adipiscing imperdiet neque..</p>
    <a class="read-more" href="#"><svg width="11" height="11" viewBox="0 0 11 11"><circle cx="5.5" cy="5.5" r="5.5" fill="#082c50"/><path d="M5.5 3v5M3 5.5h5" stroke="#fff" stroke-width="1.4"/></svg>Read More</a>
  </article>
  <div class="col-divider" style="left:598px"></div>

  <article class="service-card" style="left:618px">
    <div class="service-photo" role="img" aria-label="Photo of a crowd of people taking part in a community walk" style="background:linear-gradient(120deg,#3a8a4c,#b04050 45%,#7a6a8a 70%,#d04a7a)"></div>
    <h3>Lorem ipsum dolor</h3>
    <p>Vestibulum fermentum ultrices risus id commodo. Fusce sed ipsum ut est porta faucibus vitae luctus felis. Integer adipiscing imperdiet neque..</p>
    <a class="read-more" href="#"><svg width="11" height="11" viewBox="0 0 11 11"><circle cx="5.5" cy="5.5" r="5.5" fill="#082c50"/><path d="M5.5 3v5M3 5.5h5" stroke="#fff" stroke-width="1.4"/></svg>Read More</a>
  </article>

  <div class="info-band"></div>
  <h3 class="band-title" style="left:108px">Latest News</h3>
  <h3 class="band-title" style="left:474px">Testimonials</h3>

  <article class="news-item" style="top:740px">
    <div class="news-thumb" role="img" aria-label="Photo of a father helping his daughter with homework" style="background:linear-gradient(120deg,#6b5a48,#c7a98a 55%,#2f5a92)"></div>
    <div class="news-body">
      <h4>Lorem Ipsum comes from sections classical</h4>
      <div class="news-meta"><span>
        <svg width="8" height="7" viewBox="0 0 8 7"><ellipse cx="4" cy="3" rx="4" ry="3" fill="#ccc"/></svg>9 comments</span>
        <span><svg width="6" height="8" viewBox="0 0 6 8"><path d="M.5.5h3.5l1.5 1.5v5.5h-5z" fill="none" stroke="#ccc"/></svg>20/09/2013</span></div>
      <p>All the Lorem Ipsum generators Internet tend to repeat chunks but thenesty as necessary.</p>
      <a class="news-link" href="#">› Read more</a>
    </div>
  </article>

  <article class="news-item" style="top:837px">
    <div class="news-thumb" role="img" aria-label="Photo of a teacher working with pupils at a desk" style="background:linear-gradient(120deg,#c9a071,#e8ddd0 50%,#4f7fb8)"></div>
    <div class="news-body">
      <h4>Recently therefore sections book read always</h4>
      <div class="news-meta"><span>
        <svg width="8" height="7" viewBox="0 0 8 7"><ellipse cx="4" cy="3" rx="4" ry="3" fill="#ccc"/></svg>5 comments</span>
        <span><svg width="6" height="8" viewBox="0 0 6 8"><path d="M.5.5h3.5l1.5 1.5v5.5h-5z" fill="none" stroke="#ccc"/></svg>20/09/2013</span></div>
      <p>All the Lorem Ipsum generators Internet tend to repeat chunks but thenesty as necessary.</p>
      <a class="news-link" href="#">› Read more</a>
    </div>
  </article>

  <svg class="testimonial-tail" width="30" height="22" viewBox="0 0 30 22"><path d="M0 0L30 20H8z" fill="#ffffff"/></svg>
  <section class="testimonial-box">
    <div class="testimonial-line"></div>
    <div class="testimonial-arrow" style="left:0"><svg width="5" height="8" viewBox="0 0 5 8"><path d="M4.5.5L1 4l3.5 3.5" fill="none" stroke="#bbb"/></svg></div>
    <div class="testimonial-arrow" style="right:0"><svg width="5" height="8" viewBox="0 0 5 8"><path d="M.5.5L4 4 .5 7.5" fill="none" stroke="#bbb"/></svg></div>
    <div class="avatar" role="img" aria-label="Portrait photo of the customer"></div>
    <blockquote>Lorem Ipsum which looks reasonable generated lorem Ipsum therefore always free from repetition injected humour or non-characteristic therefore words.</blockquote>
    <div class="testimonial-author">Maren Ashby - <em>customer</em></div>
  </section>

  <div class="footer-rule"></div>
  <footer class="site-footer">
    <div class="footer-col" style="left:78px">
      <h5>INFORMATION</h5>
      <ul><li>About Us</li><li>Case studies</li><li>Engaging us</li><li>Conflict resolution App</li><li>Contact Us</li></ul>
    </div>
    <div class="footer-divider" style="left:208px"></div>
    <div class="footer-col" style="left:241px">
      <h5>OUR SERVICES</h5>
      <ul><li>Nullam mollis mi erat</li><li>Donec commodo sed justo eget</li><li>Phasellus condimentum a justo</li></ul>
      <div>nec aliquam</div>
    </div>
    <div class="footer-divider" style="left:416px"></div>
    <div class="footer-col" style="left:448px">
      <h5>CONTACT DETAILS</h5>
      <address>Harlow Brennan<br>Lorem ipsum dolor sit amet,<br>consectetur adipiscing elit.<br><br>Tel: 1200-555-0190<br>Fax: 1200-555-0191<br>Email: info@kelbrook.com.au</address>
    </div>
    <div class="footer-divider" style="left:606px"></div>
    <div class="footer-col" style="left:638px">
      <h5>NEWSLETTER SIGNUP</h5>
      <div style="line-height:14px">Lorem ipsum dolor sit amet, consectetur<br>adipiscing elit. Fusce ac nibh eu velit</div>
      <div class="newsletter-input">Enter your email address</div>
      <div class="newsletter-btn">SUBSCRIBE</div>
    </div>
  </footer>
  <div class="footer-bottom">
    <div class="copyright">Copyright © 2013 for kelbrook.com.au - All Rights reserved.</div>
    <div class="footer-social" aria-label="Social links"><span></span><span></span><span></span><span></span></div>
  </div>
</body>
</html>
```